VELINTA Promotions - Business Card Design Project

We are looking for a classy business cards for Promotion Company based in Toronto, Canada named Velinta Promotions.

Velinta Promotions has an idea and vision to set high standard, be EXCLUSIVE and attract a group of people that will follow us through events we promote (night clubs, brand promotions, music events, and sport events)

We want to present a high standards and classy image to the others...
Updates

Target Market(s)

male/female age 25-40 Target: business owners young entrepreneur - clubing industry - media industry - promotion industry - marketing media industry

Industry/Entity Type

Events

Requirements
Must have
• business cards should be classy, make people feel exclusive , make people react ..

```html
<!DOCTYPE html>
<html lang="en">
<head>
<meta charset="utf-8">
<title>Velinta Promotions – Business Card</title>
<link rel="stylesheet" href="https://fonts.googleapis.com/css2?family=Arimo:wght@700&display=swap">
<style>
  :root {
    --page: #ffffff;
    --card: #000000;
    --accent: #1cb8ec;
    --text-light: #ffffff;
    --rule: #ffffff;
  }
  html, body {
    margin: 0;
    padding: 0;
    width: 720px;
    height: 1200px;
    overflow: hidden;
    background: var(--page);
  }
  .card {
    position: absolute;
    left: 41px;
    top: 36px;
    width: 638px;
    height: 1128px;
    background: var(--card);
    overflow: hidden;
    font-family: "Arimo", Arial, sans-serif;
  }
  .brand {
    position: absolute;
    left: 0;
    right: 0;
    top: 215px;
    text-align: center;
    color: var(--accent);
    font-weight: 700;
  }
  .brand-name {
    display: block;
    font-size: 84px;
    letter-spacing: 4px;
    line-height: 1;
  }
  .brand-tagline {
    display: block;
    margin-top: 10px;
    font-size: 26px;
    letter-spacing: 9px;
    line-height: 1;
    padding-left: 150px;
  }
  .fold-line {
    position: absolute;
    left: 0;
    top: 550px;
    width: 638px;
    height: 4px;
  }
  .contact-panel {
    position: absolute;
    left: 103px;
    top: 797px;
    width: 535px;
    height: 242px;
    background: var(--accent);
    border-radius: 48px 0 0 48px;
  }
  .contact-details {
    position: absolute;
    right: 17px;
    top: 28px;
    margin: 0;
    text-align: right;
    color: var(--text-light);
    font-size: 31px;
    font-weight: 700;
    line-height: 39.5px;
    font-style: normal;
  }
  .contact-details span { display: block; }
</style>
</head>
<body>
  <main class="card">
    <div class="brand">
      <span class="brand-name">VELINTA</span>
      <span class="brand-tagline">PROMOTIONS</span>
    </div>

    <svg class="fold-line" viewBox="0 0 638 4" aria-hidden="true">
      <line x1="0" y1="2" x2="638" y2="2" stroke="var(--rule)" stroke-width="3" stroke-dasharray="14 7"/>
    </svg>

    <section class="contact-panel">
      <address class="contact-details">
        <span class="contact-name">Daniel Mercer</span>
        <span class="contact-street">1840 Harbour Rd W</span>
        <span class="contact-city">Toronto, Canada</span>
        <span class="contact-postal">M5R 3K7</span>
        <span class="contact-phone">416.555.0182</span>
      </address>
    </section>
  </main>
</body>
</html>
```